Business Card Design for The Bramblegate Apparel Company

Outlet Designer Clothing & Accessories Retailer

The Bramblegate Apparel Company is a high-end luxury outlet retailer. There is a wide selection of brands sold in the store that are from the most famous designer houses in Italy, France & Germany such

```html
<!DOCTYPE html>
<html lang="en">
<head>
<meta charset="utf-8">
<title>The Bramblegate Apparel Company – Business Card</title>
<link rel="stylesheet" href="https://fonts.googleapis.com/css2?family=Josefin+Sans:wght@400&family=Arimo:wght@400;700&family=Dancing+Script:wght@600&display=swap">
<style>
  :root {
    --backdrop: #cbcbcb;
    --card: #2c2c2c;
    --panel: #232323;
    --gold: #d9a33a;
    --ink: #1f1f1f;
    --white: #ffffff;
  }
  * { margin: 0; padding: 0; box-sizing: border-box; }
  html, body { width: 1200px; height: 505px; overflow: hidden; }
  body {
    background: var(--backdrop);
    position: relative;
    font-family: "Arimo", Arial, sans-serif;
  }
  .card {
    position: absolute;
    top: 77px;
    width: 475px;
    height: 267px;
    background: var(--card);
  }
  .card--front { left: 93px; }
  .card--back { left: 653px; }

  /* Front */
  .brand-panel {
    position: absolute;
    left: 153px; top: 23px;
    width: 160px; height: 215px;
    background: var(--panel);
    display: flex;
    flex-direction: column;
    align-items: center;
    justify-content: center;
    gap: 16px;
  }
  .brand-mark {
    width: 22px; height: 22px;
    border: 1px solid var(--white);
  }
  .brand-name {
    font-family: "Josefin Sans", sans-serif;
    font-weight: 400;
    color: var(--white);
    font-size: 14px;
    line-height: 1.45;
    letter-spacing: 2px;
    text-align: center;
    text-transform: uppercase;
  }

  /* Back */
  .bubble { position: absolute; left: 0; top: 0; }
  .bubble path { fill: var(--gold); }
  .tagline {
    position: absolute;
    left: 80px; top: 38px;
    font-family: "Dancing Script", cursive;
    font-weight: 600;
    font-size: 21px;
    color: var(--gold);
  }
  .contact-list {
    position: absolute;
    left: 170px; top: 106px;
    list-style: none;
  }
  .contact-list li {
    display: flex;
    align-items: center;
    gap: 10px;
    height: 16px;
    margin-bottom: 2px;
    font-size: 10px;
    font-weight: 700;
    color: var(--ink);
  }
  .contact-list svg { width: 13px; height: 12px; flex: none; }
  .contact-list svg * { fill: none; stroke: var(--ink); stroke-width: 1.6; }
  .contact-list svg .solid { fill: var(--ink); stroke: none; }
  .company-name {
    position: absolute;
    left: 60px; width: 360px; top: 184px;
    text-align: center;
    color: var(--white);
    font-weight: 700;
    font-size: 11px;
  }
  .company-blurb {
    position: absolute;
    left: 95px; width: 290px; top: 201px;
    text-align: center;
    color: var(--ink);
    font-size: 5.5px;
    line-height: 1.4;
  }
</style>
</head>
<body>

  <section class="card card--front">
    <div class="brand-panel">
      <span class="brand-mark"></span>
      <p class="brand-name">The<br>Bramblegate<br>Apparel<br>Company</p>
    </div>
  </section>

  <section class="card card--back">
    <svg class="bubble" width="475" height="267" viewBox="0 0 475 267" aria-hidden="true">
      <path d="M98,85 C200,80 360,80 410,83 Q432,85 432,108 L430,222 Q429,244 406,245 L84,247 Q60,247 60,224 L60,128 L74,64 L98,85 Z"/>
    </svg>
    <p class="tagline">„fashion's best kept secret"</p>

    <ul class="contact-list">
      <li>
        <svg viewBox="0 0 13 12"><path d="M1 6 H11 M7 2 L11 6 L7 10"/></svg>
        14 Ashby Row, LN7 2QB
      </li>
      <li>
        <svg viewBox="0 0 13 12"><path class="solid" d="M3 1 L5 1 L6 4 L4.5 5 Q5.5 7.5 8 8.5 L9 7 L12 8 L12 10 Q12 11 10.5 11 Q2 10 2 2 Q2 1 3 1 Z"/></svg>
        +44 020 7946 0831
      </li>
      <li>
        <svg viewBox="0 0 13 12"><rect x="1.5" y="2.5" width="10" height="7"/><path d="M1.5 2.5 L6.5 6.5 L11.5 2.5"/></svg>
        info@bramblegate.com
      </li>
      <li>
        <svg viewBox="0 0 13 12"><circle cx="6.5" cy="6" r="4.8"/><path d="M1.7 6 H11.3 M6.5 1.2 Q3.5 6 6.5 10.8 Q9.5 6 6.5 1.2"/></svg>
        www.bramblegate.com
      </li>
    </ul>

    <p class="company-name">THE BRAMBLEGATE APPAREL COMPANY</p>
    <p class="company-blurb">Designer labels from Italy, France and Germany at outlet prices, every season. Visit our store for exclusive collections and accessories curated for the discerning shopper.</p>
  </section>

</body>
</html>
```